New brand for digital company - your chance to get creative

We need to create a brand for our new business 'Lanternfish Digital'. Please read the brief below before progressing as we are looking for some quite specific outputs.

Background

We are positioning ourselves as ‘marketing technologists’ - we're helping businesses engage with their customers in the online space.

Our tactics include branding, marketing, online management, and social media, however we are differentiating ourselves by focusing on overall strategy, not just tactics. Our tagline is ‘Online made simple’.

We have stipulated some parameters for the brand but otherwise want designers to exercise their creativity.

Requirements
Must have
• We want to see an entire concept, not just a logo.

```html
<!DOCTYPE html>
<html lang="en">
<head>
<meta charset="utf-8">
<title>Lanternfish Digital – Stationery</title>
<link href="https://fonts.googleapis.com/css2?family=Ubuntu:wght@400;500;700&display=swap" rel="stylesheet">
<style>
  :root {
    --bg: #e4e4e4;
    --paper: #ffffff;
    --poster: #f1f1f1;
    --brand-red: #d81b4a;
    --folder-red: #cf1c47;
    --brand-orange: #e8891b;
  }
  * { margin: 0; padding: 0; box-sizing: border-box; }
  html, body { width: 1200px; height: 1000px; overflow: hidden; }
  body {
    position: relative;
    background: radial-gradient(ellipse at 50% 40%, #ededed 0%, var(--bg) 60%, #d4d4d4 100%);
    font-family: "Ubuntu", sans-serif;
  }

  .poster {
    position: absolute; left: 96px; top: 147px; width: 309px; height: 431px;
    background: var(--poster);
    display: flex; align-items: center; justify-content: center;
  }
  .poster__name {
    color: var(--brand-red); font-weight: 700; font-size: 44px; line-height: 1.05;
    text-align: center;
  }

  .card {
    position: absolute; width: 125px; height: 71px; background: var(--paper);
    overflow: hidden;
  }
  .card--contact { border-bottom: 3px solid var(--brand-red); }
  .card--lead { left: 456px; top: 151px; height: 75px; }
  .card__wordmark {
    position: absolute; left: 6px; top: 7px;
    color: var(--brand-red); font-weight: 700; font-size: 7px;
  }
  .card__details {
    position: absolute; left: 63px; top: 22px;
    font-size: 4px; line-height: 5.6px; color: var(--brand-orange);
    white-space: nowrap;
  }
  .card__person { color: var(--brand-red); font-weight: 700; font-size: 5px; }
  .card__role { margin-bottom: 4px; }

  .card--logo { display: flex; align-items: center; justify-content: center; gap: 4px; }
  .card__mark { width: 8px; height: 8px; background: var(--brand-red); }
  .card__name { color: var(--brand-red); font-weight: 500; font-size: 10px; }

  .col-a { left: 456px; } .col-b { left: 592px; }
  .row-1 { top: 409px; } .row-2 { top: 488px; } .row-3 { top: 567px; }

  .folder {
    position: absolute; left: 728px; top: 147px; width: 417px; height: 590px;
    background: linear-gradient(135deg, #d8214f 0%, var(--folder-red) 55%, #c41842 100%);
  }
  .letterhead {
    position: absolute; left: 39px; top: 111px; width: 309px; height: 431px;
    background: var(--paper);
  }
  .letterhead__wordmark {
    position: absolute; left: 10px; top: 12px;
    color: var(--brand-red); font-weight: 700; font-size: 9px;
  }
  .letterhead__info {
    position: absolute; top: 11px; font-size: 3.6px; line-height: 5.2px;
    color: var(--brand-red); white-space: nowrap;
  }
  .letterhead__info strong { font-weight: 700; }
  .info-address { left: 154px; }
  .info-contact { left: 198px; }
  .info-bank { left: 250px; }
</style>
</head>
<body>

  <section class="poster">
    <h1 class="poster__name">Lanternfish<br>Digital</h1>
  </section>

  <article class="card card--contact card--lead">
    <span class="card__wordmark">Lanternfish</span>
    <div class="card__details">
      <div class="card__person">Alex Marlow</div>
      <div class="card__role">Vice President</div>
      <div>t: 030 418 2290</div>
      <div>m: 0171 552 6034</div>
      <div>e: alex@lanternfish.dev</div>
      <div>w: www.lanternfish.dev</div>
    </div>
  </article>

  <article class="card card--contact col-a row-1">
    <span class="card__wordmark">Lanternfish</span>
    <div class="card__details">
      <div class="card__person">Alex Marlow</div>
      <div class="card__role">Vice President</div>
      <div>t: 030 418 2290</div>
      <div>m: 0171 552 6034</div>
      <div>e: alex@lanternfish.dev</div>
      <div>w: www.lanternfish.dev</div>
    </div>
  </article>
  <article class="card card--logo col-b row-1">
    <span class="card__mark"></span><span class="card__name">Lanternfish Digital</span>
  </article>
  <article class="card card--logo col-a row-2">
    <span class="card__mark"></span><span class="card__name">Lanternfish Digital</span>
  </article>
  <article class="card card--contact col-b row-2">
    <span class="card__wordmark">Lanternfish</span>
    <div class="card__details">
      <div class="card__person">Alex Marlow</div>
      <div class="card__role">Vice President</div>
      <div>t: 030 418 2290</div>
      <div>m: 0171 552 6034</div>
      <div>e: alex@lanternfish.dev</div>
      <div>w: www.lanternfish.dev</div>
    </div>
  </article>
  <article class="card card--contact col-a row-3">
    <span class="card__wordmark">Lanternfish</span>
    <div class="card__details">
      <div class="card__person">Alex Marlow</div>
      <div class="card__role">Vice President</div>
      <div>t: 030 418 2290</div>
      <div>m: 0171 552 6034</div>
      <div>e: alex@lanternfish.dev</div>
      <div>w: www.lanternfish.dev</div>
    </div>
  </article>
  <article class="card card--logo col-b row-3">
    <span class="card__mark"></span><span class="card__name">Lanternfish Digital</span>
  </article>

  <section class="folder">
    <article class="letterhead">
      <span class="letterhead__wordmark">Lanternfish</span>
      <div class="letterhead__info info-address">
        <div>Kastanienweg 12</div>
        <div>10405 Berlin</div>
        <div>Geschäftsführung</div>
        <div><strong>Mara Holt</strong></div>
        <div><strong>Jonas Feld</strong></div>
      </div>
      <div class="letterhead__info info-contact">
        <div>w: www.lanternfish.dev</div>
        <div>e: hello@lanternfish.dev</div>
        <div>t: 030 418 2290</div>
        <div>m: 0171 552 6034</div>
      </div>
      <div class="letterhead__info info-bank">
        <div>Steuer-Nr 00/000/00000</div>
        <div>USt-IdNr DE000000000</div>
        <div>Konto 0000 0000</div>
        <div>BLZ 000 000 00</div>
        <div>Havel Stadtbank</div>
      </div>
    </article>
  </section>

</body>
</html>
```